Need Help having my business card stand out

I am the owner of Pine Ridge Canine Coaching and would like for my business cards to stand out. I have been trying to keep designing them myself but I can't get what I have in my head on the card. I will try my best to post templates that I like for inspirations. I want something unique but elegant. I don't want in to look cartoony or cheesy. It needs to pop in a pet shop but also in a coffee shop or gym.

Target Market(s)

Dog owners, Married ,No young kids Jr High school kids and up (maybe kids on the way) Executives, Stay at home moms/wives, Small business owners

Industry/Entity Type

Dog Training

Contact Information for Business Card

Trevor Holloway, 555-304-7162, info@pineridgecanine.example, www.pineridgecanine.example

Colors

Designer to choose colors to be used in the design.

Requirements
Must have
• my logo
Should not have
• Cursive lettering

```html
<!DOCTYPE html>
<html lang="en">
<head>
<meta charset="utf-8">
<title>Pine Ridge Canine Coaching – Business Card</title>
<link rel="stylesheet" href="https://fonts.googleapis.com/css2?family=Saira:wght@400;500&display=swap">
<style>
  :root {
    --page-bg: #e9e9e9;
    --card-white: #ffffff;
    --card-black: #121212;
    --card-black-sheen: #242424;
    --ink: #111111;
    --ink-soft: #222222;
    --font-main: "Saira", "Helvetica Neue", Arial, sans-serif;
  }
  * { box-sizing: border-box; margin: 0; padding: 0; }
  html, body {
    width: 1200px;
    height: 863px;
    overflow: hidden;
    background: var(--page-bg);
  }
  .canvas {
    width: 1200px;
    height: 863px;
    display: flex;
    align-items: center;
    justify-content: center;
    gap: 90px;
  }
  .card {
    width: 350px;
    height: 612px;
    box-shadow: 0 14px 34px rgba(0, 0, 0, 0.2);
    position: relative;
    font-family: var(--font-main);
  }

  /* Front */
  .card-front {
    background: var(--card-white);
    color: var(--ink);
    display: flex;
    flex-direction: column;
    align-items: center;
    justify-content: center;
    padding: 0 32px 10px;
  }
  .brand {
    display: flex;
    flex-direction: column;
    align-items: center;
  }
  .brand-mark {
    width: 96px;
    height: 96px;
    border: 4px solid var(--ink);
    border-radius: 50%;
  }
  .brand-name {
    margin-top: 18px;
    font-weight: 500;
    font-size: 35px;
    line-height: 1.12;
    text-align: center;
    color: var(--ink);
  }
  .name-block {
    width: 238px;
    margin-top: 44px;
    border-top: 2px solid var(--ink);
    border-bottom: 2px solid var(--ink);
    padding: 9px 0 11px;
    text-align: center;
  }
  .person-name {
    font-weight: 500;
    font-size: 26px;
    letter-spacing: 0.02em;
    color: var(--ink);
  }
  .contact {
    list-style: none;
    margin-top: 20px;
    text-align: center;
    font-weight: 400;
    font-size: 16px;
    line-height: 1.45;
    color: var(--ink-soft);
  }

  /* Back */
  .card-back {
    background:
      linear-gradient(128deg, var(--card-black) 0 55%, var(--card-black-sheen) 55% 100%);
    display: flex;
    align-items: flex-start;
    justify-content: center;
    padding-top: 110px;
  }
  .emblem {
    width: 262px;
    height: 262px;
    border-radius: 50%;
    background: var(--card-white);
    border: 7px solid var(--card-white);
    box-shadow: inset 0 0 0 5px var(--card-black);
    display: flex;
    align-items: center;
    justify-content: center;
    padding: 36px;
    text-align: center;
    font-weight: 500;
    font-size: 28px;
    line-height: 1.15;
    color: var(--ink);
  }
</style>
</head>
<body>
  <main class="canvas">
    <section class="card card-front" aria-label="Business card front">
      <div class="brand">
        <span class="brand-mark" aria-hidden="true"></span>
        <p class="brand-name">Pine Ridge<br>Canine Coaching</p>
      </div>
      <div class="name-block">
        <p class="person-name">Trevor Holloway</p>
      </div>
      <ul class="contact">
        <li>555-304-7162</li>
        <li>info@pineridgecanine.example</li>
        <li>www.pineridgecanine.example</li>
      </ul>
    </section>

    <section class="card card-back" aria-label="Business card back">
      <div class="emblem">Pine Ridge Canine Coaching</div>
    </section>
  </main>
</body>
</html>
```